Business Card for Field Lotus-Eco Friendly Organic Clothing Brand

We are looking for an amazing business card for our eco friendly, organic clothing brand. We are thinking maybe a business card with a peel off sticker on the back, since our hanging clothing tag is a peel off sticker on the back. I will attach our hang tag so we can make sure we stay in line with our design. I've also attached a bag we are doing because I do like the scattered emblem look as well.

```html
<!DOCTYPE html>
<html lang="en">
<head>
<meta charset="utf-8">
<title>Field Lotus — Business Card</title>
<link href="https://fonts.googleapis.com/css2?family=Open+Sans:wght@400;600;700&display=swap" rel="stylesheet">
<style>
  :root{
    --page:#f1ede4;
    --gold-light:#e8cd86;
    --gold:#d9b24c;
    --gold-deep:#c89a2c;
    --back-gold:#e2c77e;
    --ink:#1b1b1b;
    --logo-grey:#4a4a4a;
    --camo-dark:#1f2a17;
    --camo-olive:#6f7447;
    --frame-gold:#d4ad4a;
  }
  *{margin:0;padding:0;box-sizing:border-box}
  html,body{width:1200px;height:900px;overflow:hidden}
  body{background:var(--page);position:relative;font-family:"Open Sans",Arial,sans-serif;color:var(--ink)}

  .card-front{
    position:absolute;left:238px;top:58px;width:420px;height:347px;overflow:hidden;
    background:radial-gradient(ellipse at 45% 45%,var(--gold-light) 0%,var(--gold) 60%,var(--gold-deep) 100%);
  }
  .front-logo{
    position:absolute;left:34px;top:52px;
    font-weight:700;font-size:30px;color:var(--logo-grey);line-height:1;white-space:nowrap;
  }
  .holder-name{position:absolute;left:30px;top:145px;font-weight:700;font-size:17px}
  .holder-role{position:absolute;left:30px;top:168px;font-size:14px}
  .contact-list{position:absolute;left:32px;top:208px;list-style:none;font-size:14px;line-height:21px}
  .contact-list li{display:flex;align-items:center;gap:5px}
  .contact-list svg{width:10px;height:10px;fill:var(--ink)}

  .figure-art{
    position:absolute;left:218px;top:6px;width:196px;height:335px;
    border-radius:48% 48% 10px 10px / 28% 28% 10px 10px;
    background:linear-gradient(160deg,var(--camo-olive) 0%,#a99b48 55%,#e6c232 100%);
  }

  .card-back{
    position:absolute;left:460px;top:518px;width:560px;height:342px;
    background:var(--back-gold);
  }
  .seated-cutout{
    position:absolute;left:0;top:0;width:190px;height:342px;
    background:linear-gradient(180deg,#e6cd88,#dcc077);
  }
  .sticker{
    position:absolute;left:252px;top:120px;width:242px;height:107px;
    border-radius:8px;background:var(--camo-dark);
    border:2px solid var(--frame-gold);
  }
  .sticker-mark{
    position:absolute;left:-22px;top:28px;width:48px;height:48px;
    background:var(--camo-dark);border:2px solid var(--frame-gold);
  }
  .sticker-name{
    position:absolute;left:50px;top:30px;font-weight:700;font-size:24px;color:var(--frame-gold);white-space:nowrap;
  }
  .sticker-url{
    position:absolute;left:74px;top:80px;font-size:8px;color:#f2e6c4;
  }
</style>
</head>
<body>
  <section class="card-front">
    <div class="front-logo">Field Lotus</div>
    <div class="holder-name">Daniel Archer</div>
    <div class="holder-role">Managing Director</div>
    <ul class="contact-list">
      <li><svg viewBox="0 0 10 10"><path d="M2 0h2l1 2.5-1.3 1a6 6 0 0 0 2.8 2.8l1-1.3L10 6v2a2 2 0 0 1-2 2A8 8 0 0 1 0 2a2 2 0 0 1 2-2z"/></svg>021-555 014 732</li>
      <li><svg viewBox="0 0 10 10"><path d="M0 2h10v6H0z M0 2l5 3.5L10 2" stroke="#e6cd88" stroke-width=".8"/></svg>hello@fieldlotus.com</li>
      <li><svg viewBox="0 0 10 10"><circle cx="5" cy="5" r="5"/></svg>www.fieldlotus.com</li>
    </ul>
    <div class="figure-art" role="img" aria-label="Camouflage-patterned seated meditation figure illustration"></div>
  </section>

  <section class="card-back">
    <div class="seated-cutout" role="img" aria-label="Die-cut seated meditation figure silhouette"></div>
    <div class="sticker">
      <div class="sticker-mark"></div>
      <div class="sticker-name">Field Lotus</div>
      <div class="sticker-url">www.fieldlotus.com</div>
    </div>
  </section>
</body>
</html>
```